Web Design Project (uncoded)

About Us
ZipRoam is a telecom startup and is looking to launch its website.
ZipRoam specializes in providing communication solutions to the travel market. Our mission is to develop cost effective communication products and solutions for the international traveler.
Our simple vision of "every hotel should have a mobile phone in the guest rooms", led us to develop a pathbreaking & cost effective mobile phone. With full integration capabilities with the hotels property management system, location based marketing, user locator and other features, this product is unique in addressing the hospitality segment.
The website is targeted at hotel owners and property management companies.
The website should have a young contemporary and a funky look, in line with the name.
Please find attached our logo (for the colors etc.). (attached now).
We would like to receive the design for a home page and an inside page for the website.
Site map would be as follows: Home, About Us, Solutions, Contact us
Thanks and look forward,
Tomas
Target Market(s)
Hotel decision makers
Industry/Entity Type
Property Management
Look and feel
Each slider illustrates characteristics of the customer's brand and the style your logo design should communicate.

```html
<!DOCTYPE html>
<html lang="en">
<head>
<meta charset="utf-8">
<title>ZipRoam – Home</title>
<link href="https://fonts.googleapis.com/css2?family=Arimo:wght@400;700&display=swap" rel="stylesheet">
<style>
  :root {
    --orange: #fd9a2b;
    --orange-btn: #f7931e;
    --black: #000000;
    --nav-bg: #1b1b1b;
    --nav-sep: #3a3a3a;
    --nav-text: #9a9a9a;
    --text: #222222;
    --white: #ffffff;
    --dot-idle: #f7931e;
  }
  * { box-sizing: border-box; }
  html, body {
    margin: 0;
    width: 1128px;
    height: 1200px;
    overflow: hidden;
    background: var(--white);
    font-family: "Arimo", Arial, sans-serif;
    color: var(--text);
  }
  .page { position: relative; width: 1128px; height: 1200px; }

  .header-band { position: absolute; left: 0; top: 0; width: 1128px; height: 215px; background: var(--orange); }

  .brand {
    position: absolute; left: 29px; top: 0; width: 271px; height: 107px;
    background: var(--white);
    display: flex; align-items: center; gap: 12px; padding-left: 30px;
  }
  .brand-dot { width: 52px; height: 52px; border-radius: 50%; background: var(--orange); }
  .brand-name { font-size: 38px; font-weight: 700; color: var(--text); letter-spacing: -0.5px; }

  .main-nav {
    position: absolute; left: 309px; top: 76px; width: 780px; height: 37px;
    background: var(--nav-bg);
    display: flex; align-items: center;
  }
  .main-nav a {
    display: block; height: 37px; line-height: 37px;
    font-size: 15px; color: var(--nav-text); text-decoration: none;
    text-transform: uppercase; text-align: center;
    border-right: 1px solid var(--nav-sep);
  }
  .main-nav a.is-active { color: var(--orange); }
  .nav-home { width: 111px; }
  .nav-about { width: 139px; }
  .nav-solutions { width: 147px; }
  .nav-contact { width: 157px; }
  .nav-icons { position: absolute; right: 10px; top: 9px; display: flex; gap: 18px; }

  .slider {
    position: absolute; left: 28px; top: 113px; width: 1071px; height: 479px;
    background: var(--black);
  }
  .slider-image {
    position: absolute; left: 11px; top: 12px; width: 1049px; height: 420px;
    background: linear-gradient(100deg, #d8e4f6 0%, #b9cdef 45%, #5e6f8e 70%, #2e3c52 100%);
  }
  .slider-dots { position: absolute; top: 452px; left: 509px; display: flex; gap: 8px; }
  .slider-dots span { width: 12px; height: 12px; border-radius: 50%; background: var(--dot-idle); }
  .slider-dots span.is-current { background: var(--white); }

  .welcome { position: absolute; left: 30px; top: 622px; width: 1060px; }
  .welcome h1 {
    margin: 0; font-size: 26px; font-weight: 400; color: var(--orange); text-transform: uppercase;
  }
  .welcome p { margin: 10px 0 0; font-size: 13.5px; line-height: 19.6px; }

  .btn {
    display: inline-block; height: 30px; line-height: 30px; padding: 0 9px;
    background: var(--orange-btn); color: var(--black); font-size: 11px;
    text-transform: uppercase; text-decoration: none; border-radius: 2px;
    box-shadow: 0 1px 2px rgba(0,0,0,0.35);
  }
  .welcome-more { position: absolute; left: 1006px; top: 748px; }

  .feature { position: absolute; top: 810px; width: 316px; }
  .feature h2 { margin: 0 0 12px 1px; font-size: 20px; font-weight: 400; text-transform: uppercase; color: var(--black); }
  .feature-image { width: 316px; height: 119px; }
  .feature p { margin: 13px 0 0 1px; font-size: 13.5px; line-height: 19.6px; }
  .feature .btn { position: absolute; top: 247px; left: 0; }
  .feature-travellers { left: 28px; }
  .feature-hotels { left: 406px; }
  .feature-solutions { left: 782px; }
  .feature-solutions .btn { left: -3px; }
  .img-travellers { background: linear-gradient(90deg, #7a5a48 0%, #9fb3c9 45%, #c9d6e3 100%); }
  .img-hotels { background: linear-gradient(90deg, #e6e6e0 0%, #6a4a44 40%, #2b2b2f 75%, #d9d3c2 100%); }
  .img-solutions { background: linear-gradient(90deg, #eeeeee 0%, #c9b3d6 25%, #f2c55a 60%, #e8796a 85%, #f4f4f4 100%); }

  .site-footer {
    position: absolute; left: 0; top: 1117px; width: 1128px; height: 83px;
    background: var(--black); color: var(--white);
    font-size: 11px; text-align: center; padding-top: 36px; text-transform: uppercase;
  }
</style>
</head>
<body>
<div class="page">
  <div class="header-band"></div>

  <div class="brand">
    <span class="brand-dot"></span>
    <span class="brand-name">ZipRoam</span>
  </div>

  <nav class="main-nav">
    <a class="nav-home is-active" href="#">Home</a>
    <a class="nav-about" href="#">About Us</a>
    <a class="nav-solutions" href="#">Solutions</a>
    <a class="nav-contact" href="#">Contact Us</a>
    <div class="nav-icons">
      <svg width="22" height="18" viewBox="0 0 22 18" aria-label="Phone">
        <path d="M2 6 Q11 0 20 6 L18 9 L15 7 L15 5 Q11 3 7 5 L7 7 L4 9 Z" fill="#6d6d6d"/>
        <rect x="4" y="9" width="14" height="8" rx="1" fill="#6d6d6d"/>
        <circle cx="11" cy="13" r="2.2" fill="#1b1b1b"/>
      </svg>
      <svg width="22" height="18" viewBox="0 0 22 18" aria-label="Email">
        <rect x="1" y="3" width="20" height="13" fill="#6d6d6d"/>
        <path d="M1 3 L11 11 L21 3" fill="none" stroke="#1b1b1b" stroke-width="1.5"/>
      </svg>
    </div>
  </nav>

  <section class="slider">
    <div class="slider-image" role="img" aria-label="Touchscreen mobile phone beside two young travellers with backpacks against a bright sky"></div>
    <div class="slider-dots"><span></span><span></span><span class="is-current"></span></div>
  </section>

  <section class="welcome">
    <h1>Welcome to ZipRoam</h1>
    <p>Lorem Ipsum is simply dummy text of the printing and typesetting industry. Lorem Ipsum has been the industry's standard dummy text ever since the 1500s, when an unknown printer took a galley of type and scrambled it to make a type specimen book. It has survived not only five centuries, but also the leap into electronic typesetting, remaining essentially unchanged. It was popularised in the 1960s with the release of Presslin sheets containing Lorem Ipsum passages, and more recently with desktop publishing software like Folio Layout including versions of Lorem Ipsum.</p>
  </section>
  <a class="btn welcome-more" href="#">Read More</a>

  <article class="feature feature-travellers">
    <h2>Travellers</h2>
    <div class="feature-image img-travellers" role="img" aria-label="Traveller with a backpack looking out over a cloudy sky"></div>
    <p>Lorem Ipsum is simply dummy text of the printing and typesetting industry. Lorem Ipsum has been the industry's standard dummy text</p>
    <a class="btn" href="#">Read More</a>
  </article>

  <article class="feature feature-hotels">
    <h2>Hotels</h2>
    <div class="feature-image img-hotels" role="img" aria-label="Guests checking in at a hotel reception desk"></div>
    <p>Lorem Ipsum is simply dummy text of the printing and typesetting industry. Lorem Ipsum has been the industry's standard dummy text</p>
    <a class="btn" href="#">Read More</a>
  </article>

  <article class="feature feature-solutions">
    <h2>Solutions</h2>
    <div class="feature-image img-solutions" role="img" aria-label="Colourful letter blocks spelling a word on a white grid"></div>
    <p>Lorem Ipsum is simply dummy text of the printing and typesetting industry. Lorem Ipsum has been the industry's standard dummy text</p>
    <a class="btn" href="#">Read More</a>
  </article>

  <footer class="site-footer">© 2012 ZipRoam - Terms of Service - Privacy Policy - Program Policies</footer>
</div>
</body>
</html>
```